Coffee Package Design

We need a new package design for a coffee company. Need to be a mix between modern and classic design combined together. We are open to different ideas.
We changing our product name from Café Verlona to Café Rostelli. The picture upload
shows what the product looks like. We want something completely different. The name of the company should go on the back of the package.
Updates

Hello Everyone,

Please read description, we are going with a new name and design for the product.

Café Rostelli. Café Verlona is what we are replacing with Café Rostelli, we are looking for new

look and design, please submit new designs.

There is a change in the description. Please take out Premium coffee blend and replace with Italian Roast.                                    

Industry/Entity Type

Cafe

Requirements
Must have
• You can use up to 6 colors.
Please put these items on design: Café Rostelli (this is the product name), Regular Premium Blend Coffee, 100% Arabica,
Dumbrell & Sons (name of the company), Tyler, TX on the back of the package

The file uploaded is an example of one of our products and how the package film
is sized.

```html
<!DOCTYPE html>
<html lang="en">
<head>
<meta charset="utf-8">
<title>Café Rostelli – Italian Roast Package Front</title>
<link rel="stylesheet" href="https://fonts.googleapis.com/css2?family=Oswald:wght@600&family=Lato:wght@900&display=swap">
<style>
  :root {
    --bg: #ffffff;
    --film: #1b1b1c;
    --ink: #ffffff;
    --dark-text: #1a1a1a;
    --italy-green: #2f9a3e;
    --italy-white: #eeeeee;
    --italy-red: #d9222a;
    --plaque: #f2f2f2;
  }
  html, body {
    margin: 0;
    padding: 0;
    width: 1200px;
    height: 908px;
    overflow: hidden;
    background: var(--bg);
  }
  .canvas {
    position: relative;
    width: 1200px;
    height: 908px;
  }
  .package-front {
    position: absolute;
    left: 0;
    top: 0;
  }
  .product-name {
    font-family: "Oswald", sans-serif;
    font-weight: 600;
    fill: var(--ink);
    letter-spacing: 3px;
  }
  .roast-label {
    font-family: "Oswald", sans-serif;
    font-weight: 600;
    fill: var(--dark-text);
    letter-spacing: 2px;
  }
  .arabica-badge-text {
    font-family: "Lato", sans-serif;
    font-weight: 900;
    fill: var(--dark-text);
  }
</style>
</head>
<body>
<main class="canvas">
  <svg class="package-front" width="1200" height="908" viewBox="0 0 1200 908" xmlns="http://www.w3.org/2000/svg">
    <!-- package film -->
    <rect class="film" x="270" y="0" width="725" height="908" fill="var(--film)"/>

    <!-- name block -->
    <g class="name-block">
      <circle class="name-dot" cx="610" cy="170" r="16" fill="var(--ink)"/>
      <text class="product-name" x="604" y="438" font-size="104" text-anchor="middle" textLength="560" lengthAdjust="spacingAndGlyphs">CAFÉ ROSTELLI</text>
    </g>

    <!-- roast plaque -->
    <g class="roast-plaque">
      <rect x="418" y="483" width="372" height="64" rx="12" fill="var(--plaque)" stroke="var(--film)" stroke-width="3"/>
      <circle cx="433" cy="515" r="4" fill="var(--film)"/>
      <circle cx="775" cy="515" r="4" fill="var(--film)"/>
      <text class="roast-label" x="604" y="533" font-size="44" text-anchor="middle" textLength="318" lengthAdjust="spacingAndGlyphs">ITALIAN ROAST</text>
    </g>

    <!-- tricolour stripe -->
    <g class="tricolour-stripe">
      <rect x="520" y="553" width="185" height="355" fill="var(--ink)"/>
      <rect x="530" y="553" width="55" height="355" fill="var(--italy-green)"/>
      <rect x="585" y="553" width="55" height="355" fill="var(--italy-white)"/>
      <rect x="640" y="553" width="55" height="355" fill="var(--italy-red)"/>
    </g>

    <!-- arabica badge -->
    <g class="arabica-badge" transform="rotate(-12 738 622)">
      <polygon fill="var(--plaque)" points="
        738,552 752,562 768,556 777,571 794,572 796,589 811,597 806,613 816,627 806,641 811,657 796,665 794,682 777,683 768,698 752,692 738,702 724,692 708,698 699,683 682,682 680,665 665,657 670,641 660,627 670,613 665,597 680,589 682,572 699,571 708,556 724,562"/>
      <text class="arabica-badge-text" x="738" y="628" font-size="34" text-anchor="middle">100%</text>
      <rect x="690" y="636" width="96" height="2" fill="var(--dark-text)"/>
      <text class="arabica-badge-text" x="738" y="662" font-size="22" text-anchor="middle">ARABICA</text>
    </g>
  </svg>
</main>
</body>
</html>
```